Stationery Design Project

I am looking for stationary design for an automotive collision repair company. This needs to work with my business cards just designed here. I've attached. I need 8.5 x 11 stationary and corissponding envelopes. a jot tab note pad also. Our companies focus is very high end customer service driven . Our customer base is 35-65 middle to high income. Please include company name, logo, address, phone number, web address. The business card is two greys with green and white writing. I invision a light grey background with a darker grey band on it that contains the logo.
Updates

I justĀ 

Why is no one touching this project

Target Market(s)

60%. Women 40% men. Age 35-60

Industry/Entity Type

Automotive

Requirements
Must have
• Tie in with business cards. So it needs grey tones with green and white logo. Name, address, phone and web address. Must have 8.5 x 11 paper and envelopes.
Nice to have
• Jot tab notes

```html
<!DOCTYPE html>
<html lang="en">
<head>
<meta charset="utf-8">
<title>Panelcraft Auto — Stationery Set</title>
<link rel="stylesheet" href="https://fonts.googleapis.com/css2?family=Arimo:wght@400;700&display=swap">
<style>
  :root {
    --paper: #ffffff;
    --grey-top: #d2d2d2;
    --grey-mid: #e8e8e8;
    --accent: #80ff00;
    --accent-soft: #d9ffb3;
    --swoosh-grey: #cfcfcf;
    --ink: #111111;
    --frame: #333333;
    --sheet-edge: #9a9a9a;
  }
  * { box-sizing: border-box; margin: 0; padding: 0; }
  html, body { width: 1200px; height: 724px; overflow: hidden; background: var(--paper); }
  body { font-family: "Arimo", Arial, sans-serif; color: var(--ink); }

  .canvas {
    position: relative; width: 1200px; height: 724px;
    border: 1px solid var(--frame); background: var(--paper);
  }

  .brand-name {
    position: absolute; font-weight: 700; color: var(--accent);
    letter-spacing: -0.3px; line-height: 1;
  }

  .contact { position: absolute; font-size: 8.3px; line-height: 13px; white-space: nowrap; }
  .contact.right { text-align: right; }

  .swoosh-band { position: absolute; }

  /* Envelope front */
  .envelope-front {
    position: absolute; left: 40px; top: 82px; width: 541px; height: 227px;
  }
  .envelope-front .shade {
    position: absolute; inset: 0 0 -6px 0;
    background: linear-gradient(to bottom, var(--grey-top), var(--paper));
  }
  .envelope-front .brand-name { left: 23px; top: 32px; font-size: 14px; }
  .envelope-front .swoosh-band { left: 10px; top: 140px; width: 528px; height: 70px; }
  .envelope-front .contact.left { left: 24px; top: 203px; }
  .envelope-front .contact.right { right: 28px; top: 200px; }

  /* Envelope back */
  .envelope-back {
    position: absolute; left: 48px; top: 372px; width: 541px; height: 236px;
    border: 1px solid var(--frame); background: var(--paper);
  }
  .envelope-back svg { position: absolute; left: -2px; top: -1px; }

  /* Letterhead */
  .letterhead {
    position: absolute; left: 649px; top: 27px; width: 517px; height: 670px;
    border: 1px solid var(--sheet-edge);
    background: linear-gradient(to bottom, var(--grey-top) 0%, var(--grey-mid) 45%, var(--paper) 90%);
  }
  .letterhead .brand-name { left: 45px; top: 63px; font-size: 18px; }
  .letterhead .swoosh-band { left: 12px; top: 543px; width: 500px; height: 75px; }
  .letterhead .contact.left { left: 30px; top: 623px; font-size: 8.6px; line-height: 17px; }
  .letterhead .contact.right { right: 36px; top: 613px; font-size: 8.6px; line-height: 17px; }
</style>
</head>
<body>
<main class="canvas">

  <section class="envelope-front" aria-label="Envelope front">
    <div class="shade"></div>
    <span class="brand-name">Panelcraft Auto</span>
    <svg class="swoosh-band" viewBox="0 0 528 70" role="img" aria-label="Decorative green and grey brand sweep">
      <defs>
        <linearGradient id="sweep-env" x1="0" y1="0" x2="1" y2="0">
          <stop offset="0" stop-color="var(--accent-soft)" stop-opacity="0.4"/>
          <stop offset="0.6" stop-color="var(--swoosh-grey)"/>
          <stop offset="1" stop-color="var(--accent-soft)"/>
        </linearGradient>
      </defs>
      <rect x="0" y="30" width="528" height="34" rx="17" fill="url(#sweep-env)"/>
    </svg>
    <p class="contact left">Panelcraft Auto<br>88 Fender Lane Bodyworks 3120</p>
    <p class="contact right">M: 0400 123 456 T: 03 5550 1234<br>E: mia@panelcraftauto.com W: www.panelcraftauto.com</p>
  </section>

  <section class="envelope-back" aria-label="Envelope back">
    <svg width="545" height="96" viewBox="0 0 545 96" aria-hidden="true">
      <polygon class="flap" points="0,0 543,0 543,75 535,94 20,93 7,80 3,30" fill="var(--accent)"/>
    </svg>
  </section>

  <section class="letterhead" aria-label="Letterhead">
    <span class="brand-name">Panelcraft Auto</span>
    <svg class="swoosh-band" viewBox="0 0 500 75" role="img" aria-label="Decorative green and grey brand sweep">
      <defs>
        <linearGradient id="sweep-sheet" x1="0" y1="0" x2="1" y2="0">
          <stop offset="0" stop-color="var(--accent-soft)" stop-opacity="0.4"/>
          <stop offset="0.6" stop-color="var(--swoosh-grey)"/>
          <stop offset="1" stop-color="var(--accent-soft)"/>
        </linearGradient>
      </defs>
      <rect x="0" y="32" width="500" height="36" rx="18" fill="url(#sweep-sheet)"/>
    </svg>
    <p class="contact left">M: 0400 123 456 T: 03 5550 1234<br>E: mia@panelcraftauto.com W: www.panelcraftauto.com</p>
    <p class="contact right">Panelcraft Auto<br>88 Fender Lane Bodyworks 3120</p>
  </section>

</main>
</body>
</html>
```